Country Music Cruise Design

Current site
www.mapleharbors.com/index.php

We want a site that is Vibrant and Colorful with cartoon style graphics. This will be a bootstrap site and shall use that idea when designing.

We want a mixture of the two sites which we really like
http://www.ridgelinegetaway.com/
and
https://quilbymeet.net

Our logo is attached
Need a really nice one page design homepage with information and one page for the booking (www.mapleharbors.com/book)

country music fans on a cruise ship, 20-50 year old

4 page

Sans Serif

• Vibrant style colors and backgrounds like examples above.
• Dark color

```html
<!DOCTYPE html>
<html lang="en">
<head>
<meta charset="utf-8">
<title>Harbor Twang Cruise</title>
<link rel="stylesheet" href="https://fonts.googleapis.com/css2?family=Bitter:wght@400;700;800&family=Open+Sans:wght@600;700&family=Noto+Serif:wght@400&display=swap">
<style>
:root{
  --sky-top:#2fa6e6;
  --sky-mid:#7cc7ec;
  --sky-low:#f5a07a;
  --sea:#1f7fd0;
  --red:#d42027;
  --green:#16a848;
  --yellow:#e2c524;
  --wood:#3e2c1f;
  --parchment:#f2dfb3;
  --board:#c98c4d;
  --paper:#f7f7f7;
  --ink:#111;
  --footer:#2b2a29;
  --footer-line:#403e3b;
  --gold:#f0c419;
  --muted:#b5ab93;
  --cream:#f3ead0;
}
*{margin:0;padding:0;box-sizing:border-box}
html,body{width:1200px;height:2394px;overflow:hidden}
body{position:relative;background:var(--footer);font-family:"Noto Serif",serif;color:var(--ink)}
.abs{position:absolute}

/* hero */
.hero{left:0;top:0;width:1200px;height:560px;background:linear-gradient(180deg,var(--sky-top) 0%,var(--sky-mid) 42%,var(--sky-low) 72%,var(--sea) 100%)}
.search{left:172px;top:32px;width:519px;height:37px;background:#fff;border-radius:4px;box-shadow:0 2px 4px rgba(0,0,0,.25)}
.search span{position:absolute;left:35px;top:11px;font:600 11px "Open Sans",sans-serif;color:#555;letter-spacing:.3px}
.search-btn{position:absolute;right:3px;top:3px;width:45px;height:31px;background:#f5d40f;border-radius:3px}
.btn{display:flex;align-items:center;justify-content:center;background:var(--green);color:#fff;font:700 14px "Open Sans",sans-serif;letter-spacing:.6px;border-radius:6px;box-shadow:0 0 0 5px #fff,0 3px 8px rgba(0,0,0,.3)}
.btn-top{left:886px;top:34px;width:136px;height:32px}
.nav{left:172px;top:83px;width:854px;height:42px;background:var(--red);display:flex;align-items:center;padding-left:54px}
.nav a{font:700 13px "Open Sans",sans-serif;color:#fff;text-decoration:none;margin-right:44px}
.social{position:absolute;right:10px;top:9px;display:flex;align-items:center;gap:9px;font:700 11px "Open Sans",sans-serif;color:#fff;letter-spacing:.4px}
.social i{display:block;width:25px;height:25px;background:#fff;border-radius:2px}
.brand-hero{left:598px;top:262px;width:503px;text-align:center;font:800 62px/1.05 "Bitter",serif;color:var(--gold)}

/* date band */
.band{left:0;top:551px;width:1200px;height:480px;background:var(--yellow)}
.band-art{left:0;top:600px;width:1200px;height:420px;background:radial-gradient(ellipse at 50% 50%,rgba(176,150,30,.3),rgba(176,150,30,0) 70%)}
.band-title{left:0;top:636px;width:1200px;text-align:center;font:800 72px/92px "Bitter",serif;color:var(--ink)}
.band-sub{left:0;top:830px;width:1200px;text-align:center;font:700 15px "Bitter",serif;letter-spacing:.3px}
.btn-band{left:511px;top:894px;width:178px;height:40px}

/* info boards */
.wood{left:0;top:1030px;width:1200px;height:445px;background:linear-gradient(180deg,#4a3525,var(--wood) 50%,#34251a)}
.board{top:1133px;width:277px;height:240px;background:var(--board);border-radius:4px;box-shadow:0 4px 10px rgba(0,0,0,.5);padding:14px}
.board-inner{width:100%;height:100%;background:var(--parchment);border-radius:3px;text-align:center;padding:24px 14px 0;position:relative}
.board h3{font:800 22px "Bitter",serif;color:#1a1208;margin-bottom:10px}
.board p{font:400 11.5px/18px "Noto Serif",serif;color:#2a1d10}
.nail{position:absolute;top:-6px;width:12px;height:12px;border-radius:50%;background:#9a9a9a;left:50%;margin-left:-6px}
.pin{position:absolute;bottom:-6px;left:50%;margin-left:-8px;width:16px;height:16px;border-radius:50%;background:var(--red)}

/* about */
.about{left:0;top:1468px;width:1200px;height:320px;background:var(--paper)}
.about h2{position:absolute;left:0;top:88px;width:1200px;text-align:center;font:800 32px "Bitter",serif}
.about p{position:absolute;left:194px;top:144px;width:812px;text-align:center;font:400 13px/24px "Noto Serif",serif;color:#333}

/* footer */
.foot-brand{left:160px;top:1870px;width:290px;font:800 40px/1.05 "Bitter",serif;color:var(--gold);display:flex;align-items:center;gap:14px}
.foot-brand i{flex:none;width:34px;height:34px;border-radius:50%;background:var(--gold)}
.sub-title{left:528px;top:1864px;font:700 19px "Bitter",serif;color:#fff;letter-spacing:.2px}
.sub-input{left:528px;top:1904px;width:367px;height:43px;background:var(--cream);display:flex;align-items:center;padding-left:52px;font:400 12.5px "Noto Serif",serif;color:#333}
.sub-btn{left:906px;top:1904px;width:131px;height:43px;background:var(--cream);clip-path:polygon(0 0,88% 0,100% 50%,88% 100%,0 100%);font:700 16px "Bitter",serif;display:flex;align-items:center;padding-left:30px}
.contact{left:531px;top:1968px;width:380px;height:116px;border-left:3px double #8a8270;padding-left:28px}
.contact div{font:400 11.5px/18px "Noto Serif",serif;color:var(--muted);margin-bottom:12px;display:flex;gap:14px;align-items:flex-start}
.contact svg{flex:none}
.col h4{font:700 16px "Bitter",serif;color:var(--gold);margin-bottom:18px;letter-spacing:.2px}
.col p,.col li{font:400 11.5px/22px "Noto Serif",serif;color:var(--muted);list-style:none}
.col-about{left:160px;top:2144px;width:360px}
.col-nav{left:598px;top:2144px;width:260px}
.col-nav ul{display:grid;grid-template-columns:160px 100px}
.col-keys{left:876px;top:2144px;width:200px}
.rule{left:0;top:2340px;width:1200px;height:1px;background:var(--footer-line)}
.copy{left:0;top:2360px;width:1200px;text-align:center;font:400 11px "Noto Serif",serif;color:var(--muted)}
.copy b{color:var(--gold);font-weight:400}
</style>
</head>
<body>

<header>
  <div class="abs hero" role="img" aria-label="Cartoon pirate ship sailing on waves under a sunset sky"></div>
  <div class="abs search"><span>SEARCH HERE...</span><div class="search-btn">
    <svg width="45" height="31" viewBox="0 0 45 31"><circle cx="21" cy="14" r="6" fill="none" stroke="#fff" stroke-width="2.5"/><line x1="25.5" y1="18.5" x2="30" y2="23" stroke="#fff" stroke-width="2.5"/></svg>
  </div></div>
  <div class="abs btn btn-top">BOOK NOW</div>
  <nav class="abs nav">
    <a>Prices</a><a>What's Included?</a><a>FAQ's</a><a>Shop</a><a>Book Now</a>
    <div class="social">SOCIAL LINKS :<i aria-label="Social link"></i><i aria-label="Social link"></i><i aria-label="Social link"></i><i aria-label="Social link"></i></div>
  </nav>
  <div class="abs brand-hero">Harbor Twang Cruise</div>
</header>

<section>
  <div class="abs band"></div>
  <div class="abs band-art" role="img" aria-label="Faint sketch of a ship wheel and sailing ship"></div>
  <svg class="abs" style="left:0;top:536px" width="1200" height="30" viewBox="0 0 1200 30"><polygon fill="#e2c524" points="0,30 0,12 60,18 130,8 210,16 300,6 380,15 470,9 560,17 650,7 740,14 830,5 920,15 1010,8 1100,16 1200,9 1200,30"/></svg>
  <h1 class="abs band-title">HTC 2018 - JAN<br>12-15TH 2018</h1>
  <div class="abs band-sub">DON'T BE LEFT ON SHORE!</div>
  <div class="abs btn btn-band">BOOK NOW</div>
</section>

<section>
  <div class="abs wood"></div>
  <svg class="abs" style="left:0;top:1015px" width="1200" height="30" viewBox="0 0 1200 30"><polygon fill="#4a3525" points="0,30 0,18 80,10 160,20 250,8 340,17 430,11 520,20 610,9 700,18 790,12 880,21 970,9 1060,17 1140,10 1200,16 1200,30"/></svg>
  <div class="abs board" style="left:160px"><div class="board-inner"><span class="nail"></span><h3>What's Included?</h3><p>All HTC events, Food, Comedy Club, Kids Clubs, Game Shows, Night Clubs, GYM, Bars and Water Park</p><span class="pin"></span></div></div>
  <div class="abs board" style="left:461px"><div class="board-inner"><span class="nail"></span><h3>HTC Activities</h3><p>We will bring on bands, Southern California's favorite DJ's, Line Dance Lessons, Two Stepping, Contest, Offshore Parties and much much more</p><span class="pin"></span></div></div>
  <div class="abs board" style="left:763px"><div class="board-inner"><span class="nail"></span><h3>Ship Itinerary</h3><p>January 12th -15th<br>Friday - Leave Port 5:30 PM<br>Saturday - Ensenada Mexico | Formal Dinner<br>Sunday - Day at Sea</p><span class="pin"></span></div></div>
</section>

<section class="abs about">
  <h2>HTC 2018 - JAN 12-15TH 2018</h2>
  <p>Country and Cruising? Don't miss out on this excursion that is 3 Nights – 2 Days on January 12th - 15th 2018 out of Long Beach. This cruise will be taken over by our West Coast Country family. We are putting boots onboard for two stepping, line dancing, multiple bands and our favorite Southern California Country DJ to bring it all together. Includes all food onboard, dance lessons, concerts, all ship activities and contest. DON'T WAIT! Rates will go up!</p>
</section>
<svg class="abs" style="left:0;top:1452px" width="1200" height="30" viewBox="0 0 1200 30"><polygon fill="#f7f7f7" points="0,30 0,14 70,20 150,8 240,18 330,10 420,21 510,7 600,17 690,11 780,20 870,8 960,18 1050,10 1130,19 1200,12 1200,30"/></svg>
<svg class="abs" style="left:0;top:1772px" width="1200" height="30" viewBox="0 0 1200 30"><polygon fill="#2b2a29" points="0,30 0,12 90,20 170,9 260,18 350,8 440,19 530,11 620,21 710,8 800,17 890,10 980,20 1070,9 1150,18 1200,11 1200,30"/></svg>

<footer>
  <div class="abs foot-brand"><i></i>Harbor Twang Cruise</div>
  <div class="abs sub-title">SUBSCRIBE TO GET NEW DISCOUNT</div>
  <div class="abs sub-input">
    <svg class="abs" style="left:16px;top:13px" width="22" height="17" viewBox="0 0 22 17"><rect x="1" y="1" width="20" height="15" fill="none" stroke="#555" stroke-width="1.5"/><polyline points="1,1 11,9 21,1" fill="none" stroke="#555" stroke-width="1.5"/></svg>
    Enter Your E-mail Here..
  </div>
  <div class="abs sub-btn">Subscribe</div>
  <div class="abs contact">
    <div><svg width="18" height="18" viewBox="0 0 18 18"><rect x="2" y="2" width="14" height="14" fill="none" stroke="#8a8270" stroke-width="1.5"/><line x1="2" y1="6" x2="16" y2="6" stroke="#8a8270" stroke-width="1.5"/></svg><span>JAN 18TH - 21ST 2019 (WINTER HOLIDAY<br>WEEKEND)</span></div>
    <div><svg width="18" height="18" viewBox="0 0 18 18"><path d="M4 2 L7 2 L8 6 L6 7 Q8 11 11 12 L12 10 L16 11 L16 14 Q10 16 5 10 Q2 6 4 2Z" fill="#8a8270"/></svg><span>PHONE &nbsp;// &nbsp;1-4820-17390</span></div>
    <div><svg width="18" height="18" viewBox="0 0 18 18"><path d="M2 3 H16 V12 H7 L3 15 V12 H2Z" fill="#8a8270"/></svg><span>E-mail &nbsp;// &nbsp;info@mapleharbors.com</span></div>
  </div>

  <div class="abs col col-about"><h4>HARBOR TWANG CRUISE</h4><p>Country and Cruising? Don't miss out on this excursion that is 3 Nights – 2 Days on January 12th - 15th 2018 out of Long Beach. This cruise will be taken over by our West Coast Country family. We are putting boots onboard for two-step-ping, line dancing, multiple bands and our favorite Southern California Country DJ to bring it all together.</p></div>
  <div class="abs col col-nav"><h4>NAVIGATION</h4><ul><li>Prices</li><li>Sponsors</li><li>Pics &amp; Vids</li><li>About</li><li>Press</li><li></li><li>FAQ's</li><li></li><li>Vendors</li></ul></div>
  <div class="abs col col-keys"><h4>KEY FEATURES</h4><ul><li>1 &nbsp;Live Bands</li><li>2 &nbsp;Line Dancing</li><li>3 &nbsp;Contest</li><li>4 &nbsp;All you can drink packages</li></ul></div>
  <div class="abs rule"></div>
  <div class="abs copy">Copyright ©2018 <b>Harbor Twang Cruise</b> . All Rights Reserved</div>
</footer>

</body>
</html>
```